Rise Past Horizon needs a new design for Business Cards

We need a business card design for our personal training business call Rise Past Horizon. We are the Sustained Weight Loss Specialists.
Our target market is overweight and obese adults who have experience the ups of loosing weight and lows of putting it back on and are looking for a sustained weight loss solution.
Our USP is: "We Smash Through The Barriers That Are Holding You Back From Sustained Weight Loss".
We would like to the design incorporate the colours of our logo, with other acceptable colours being black, white, yellow and green.
Visit our website at www.risepasthorizon.com.au for an overview of our business, and also the attached company profile.

Target Market(s)

Industry/Entity Type

Training

Colors
0092cd
eb1f27
fbed22
9bcb3c
000000
ffffff

Requirements
Must have
• Easy to read fonts
Logo (Not huge)
Call to Action (Something like, Claim your 10 Tips to Melt Body Fat, and 30 minutes PT Session VALUED AT $101)
Contact and Address details (as per footer of company profile (page 2 onwards)
List of Benefits (see company profile and website)
USP as per project overview
A picture to match the USP
Should not have
• Please do not try and copy the design of the company profile. It was slapped together.
A list of exercises

```html
<!DOCTYPE html>
<html lang="en">
<head>
<meta charset="utf-8">
<title>Rise Past Horizon — Business Card</title>
<link href="https://fonts.googleapis.com/css2?family=Oswald:wght@500&family=Roboto+Condensed:wght@400;700&display=swap" rel="stylesheet">
<style>
  :root {
    --brand-blue: #2f7fc9;
    --brand-blue-deep: #2569ad;
    --brand-red: #eb1f27;
    --card-white: #ffffff;
    --ink: #4a4a4a;
    --stage: #e9e9e9;
  }
  * { box-sizing: border-box; margin: 0; padding: 0; }
  html, body {
    width: 1200px; height: 682px; overflow: hidden;
    background: var(--stage);
    font-family: "Roboto Condensed", sans-serif;
  }
  .card {
    position: absolute; top: 187px;
    width: 540px; height: 308px;
    overflow: hidden;
    box-shadow: 0 6px 18px rgba(0,0,0,.18);
  }

  /* ---------- Front ---------- */
  .card-front { left: 40px; background: var(--card-white); }
  .top-band {
    position: absolute; left: 0; top: 0; width: 100%; height: 14px;
    background: var(--brand-blue);
  }
  .brand {
    position: absolute; left: 70px; top: 34px;
    display: flex; flex-direction: column; align-items: center; gap: 8px;
  }
  .brand-art {
    width: 104px; height: 70px; border-radius: 5px;
    background: linear-gradient(135deg, #3d86cf, #2f7fc9 60%, #5d9ad6);
  }
  .brand-name {
    display: flex; align-items: center; gap: 5px;
    color: var(--brand-red);
    font-weight: 400; font-size: 13px; letter-spacing: 1px; text-transform: uppercase;
    white-space: nowrap;
  }
  .brand-dot { width: 6px; height: 6px; border-radius: 50%; background: var(--brand-red); }
  .name-band {
    position: absolute; left: 30px; right: 0; top: 150px; height: 30px;
    background: var(--brand-blue);
    display: flex; align-items: center; justify-content: space-between;
    padding-right: 22px;
    color: var(--card-white);
  }
  .name-group { display: flex; align-items: center; height: 100%; }
  .icon-box {
    width: 30px; height: 30px; background: var(--brand-red);
    display: flex; align-items: center; justify-content: center;
    border: 3px solid var(--card-white);
    margin-right: 10px;
  }
  .person-name {
    font-family: "Oswald", sans-serif; font-weight: 500;
    font-size: 18px; letter-spacing: 1.2px; text-transform: uppercase;
  }
  .job-title { font-size: 12px; letter-spacing: 1.2px; text-transform: uppercase; }
  .contacts {
    position: absolute; left: 70px; top: 196px;
    display: grid; grid-template-columns: 170px 220px; row-gap: 10px;
    color: var(--ink); font-size: 11px; letter-spacing: .3px;
  }
  .contact { display: flex; align-items: center; gap: 7px; white-space: nowrap; }
  .contact svg { flex: none; }
  .address-band {
    position: absolute; left: 0; right: 0; top: 252px; height: 26px;
    background: var(--brand-red); color: var(--card-white);
    display: flex; align-items: center; gap: 7px; padding-left: 40px;
    font-size: 11px; letter-spacing: .3px;
  }
  .bottom-band {
    position: absolute; left: 0; right: 0; top: 283px; height: 10px;
    background: var(--brand-blue);
  }

  /* ---------- Back ---------- */
  .card-back {
    left: 620px;
    background: var(--brand-blue);
    color: var(--card-white);
  }
  .back-brand {
    position: absolute; left: 24px; top: 22px;
    display: flex; align-items: center; gap: 5px;
    font-size: 12px; letter-spacing: 1px; text-transform: uppercase;
  }
  .back-brand .brand-dot { background: var(--card-white); }
  .usp {
    position: absolute; left: 24px; top: 44px; width: 290px;
    font-family: "Oswald", sans-serif; font-weight: 500;
    font-size: 18px; line-height: 1.2; text-transform: uppercase; letter-spacing: .4px;
  }
  .benefits {
    position: absolute; left: 24px; top: 146px; width: 290px;
    list-style: none; display: grid; row-gap: 6px;
    font-size: 12px; letter-spacing: .3px;
  }
  .benefit { display: flex; align-items: center; gap: 7px; }
  .benefit svg { flex: none; }
  .usp-photo {
    position: absolute; right: 24px; top: 22px;
    width: 176px; height: 196px; border-radius: 4px;
    background: linear-gradient(160deg, #5d9ad6, var(--brand-blue-deep));
    border: 3px solid var(--card-white);
  }
  .cta-band {
    position: absolute; left: 0; right: 0; top: 234px; height: 48px;
    background: var(--brand-red);
    display: flex; flex-direction: column; justify-content: center;
    padding-left: 24px;
    font-size: 12px; letter-spacing: .3px; line-height: 1.35;
  }
  .cta-lead { font-weight: 700; text-transform: uppercase; }
  .back-bottom-band {
    position: absolute; left: 0; right: 0; top: 287px; height: 10px;
    background: var(--card-white);
  }
</style>
</head>
<body>
  <main class="card card-front">
    <div class="top-band"></div>

    <div class="brand">
      <div class="brand-art" role="img" aria-label="Brand illustration area in brand blue"></div>
      <div class="brand-name"><span class="brand-dot"></span>Rise Past Horizon</div>
    </div>

    <div class="name-band">
      <div class="name-group">
        <div class="icon-box">
          <svg width="13" height="13" viewBox="0 0 24 24" aria-hidden="true">
            <circle cx="12" cy="8" r="5" fill="#fff"/>
            <path d="M2 23c0-6 4.5-9 10-9s10 3 10 9z" fill="#fff"/>
          </svg>
        </div>
        <span class="person-name">Dana Whitfield</span>
      </div>
      <span class="job-title">General Manager</span>
    </div>

    <div class="contacts">
      <div class="contact">
        <svg width="11" height="11" viewBox="0 0 24 24" aria-hidden="true"><path d="M6.6 10.8a15 15 0 0 0 6.6 6.6l2.2-2.2a1 1 0 0 1 1-.25 11.4 11.4 0 0 0 3.6.57 1 1 0 0 1 1 1V20a1 1 0 0 1-1 1A17 17 0 0 1 3 4a1 1 0 0 1 1-1h3.5a1 1 0 0 1 1 1c0 1.25.2 2.45.57 3.57a1 1 0 0 1-.25 1z" fill="#eb1f27"/></svg>
        <span>013 482 5170</span>
      </div>
      <div class="contact">
        <svg width="11" height="11" viewBox="0 0 24 24" aria-hidden="true"><rect x="2" y="5" width="20" height="14" rx="1" fill="#eb1f27"/><path d="M2 6l10 7 10-7" fill="none" stroke="#fff" stroke-width="2"/></svg>
        <span>hello@mailbox.com</span>
      </div>
      <div class="contact">
        <svg width="11" height="11" viewBox="0 0 24 24" aria-hidden="true"><rect x="6" y="2" width="12" height="20" rx="2" fill="none" stroke="#eb1f27" stroke-width="2.4"/><circle cx="12" cy="18" r="1.4" fill="#eb1f27"/></svg>
        <span>013 482 5170</span>
      </div>
      <div class="contact">
        <svg width="11" height="11" viewBox="0 0 24 24" aria-hidden="true"><circle cx="12" cy="12" r="10" fill="#eb1f27"/><path d="M2 12h20M12 2c3 3 3 17 0 20M12 2c-3 3-3 17 0 20" fill="none" stroke="#fff" stroke-width="1.4"/></svg>
        <span>www.risepasthorizon.com.au</span>
      </div>
    </div>

    <div class="address-band">
      <svg width="10" height="13" viewBox="0 0 24 30" aria-hidden="true"><path d="M12 0a10 10 0 0 0-10 10c0 8 10 20 10 20s10-12 10-20A10 10 0 0 0 12 0z" fill="#fff"/><circle cx="12" cy="10" r="4" fill="#eb1f27"/></svg>
      <span>214 Kerrin Avenue, Level 2 Suite 5</span>
    </div>
    <div class="bottom-band"></div>
  </main>

  <section class="card card-back">
    <div class="back-brand"><span class="brand-dot"></span>Rise Past Horizon</div>

    <h2 class="usp">We Smash Through The Barriers That Are Holding You Back From Sustained Weight Loss</h2>

    <ul class="benefits">
      <li class="benefit">
        <svg width="11" height="11" viewBox="0 0 24 24" aria-hidden="true"><path d="M3 12l6 6L21 6" fill="none" stroke="#fff" stroke-width="3.5"/></svg>
        Sustained weight loss specialists
      </li>
      <li class="benefit">
        <svg width="11" height="11" viewBox="0 0 24 24" aria-hidden="true"><path d="M3 12l6 6L21 6" fill="none" stroke="#fff" stroke-width="3.5"/></svg>
        One-on-one personal training
      </li>
      <li class="benefit">
        <svg width="11" height="11" viewBox="0 0 24 24" aria-hidden="true"><path d="M3 12l6 6L21 6" fill="none" stroke="#fff" stroke-width="3.5"/></svg>
        Nutrition and lifestyle coaching
      </li>
    </ul>

    <div class="usp-photo" role="img" aria-label="Photo of a client breaking through a barrier"></div>

    <div class="cta-band">
      <span class="cta-lead">Claim your 10 Tips to Melt Body Fat</span>
      <span>plus a 30 minute PT session, valued at $101</span>
    </div>
    <div class="back-bottom-band"></div>
  </section>
</body>
</html>
```